Appraisal and Umpire Services for Property Damage Insurance Claims

I need a banner design that I can post as an advertisement on industry web pages. I would like this to be elegant and reflective of quality, integrity and professionalism.

Target Market(s)

Insurance Companies and Attorneys

Industry/Entity Type

Insurance

Contact Information for Business Card

Gerald M. Hollis
918 Birchwell Lane
PO Box 582
Clifton Park, NY 12093
ghollis@brindlevault.com
Phone: (800) 555-0147, Ext. 2861
Direct: (315) 555-0189

Logo Text

Line One: Velmar Brook Claim Service, Inc. Line two: Appraisal and Umpire Services

Font styles to use
Serif
Sans Serif

Colors
0255a3
f78f20
faa54b
3176b5

Requirements
Must have
• New Logo and matching banner, business card and stationary.
• The colors must be orange and navy blue in the logo. I have selected them below.

```html
<!DOCTYPE html>
<html lang="en">
<head>
<meta charset="utf-8">
<title>Velmar Brook Claim Service, Inc. — Banner</title>
<link rel="stylesheet" href="https://fonts.googleapis.com/css2?family=Barlow:wght@600&family=Fira+Sans+Extra+Condensed:wght@700&display=swap">
<style>
  :root {
    --peach: #f9cf86;
    --peach-light: #fbd68f;
    --umber: #3b2e1f;
    --navy-ink: #111626;
    --brand-orange: #e8561e;
    --burnt-orange: #cf6a24;
    --tag-ink: #1b1410;
    --white: #ffffff;
    --alarm-red: #e01e1e;
    --frame-orange: #e2762a;
    --frame-white: #f2f2f2;
  }
  * { margin: 0; padding: 0; box-sizing: border-box; }
  html, body { width: 1200px; height: 386px; overflow: hidden; background: #ffffff; }
  .banner {
    position: relative;
    width: 1200px;
    height: 386px;
    overflow: hidden;
    background: linear-gradient(90deg, var(--peach) 0%, var(--peach) 46%, #c9a266 56%, #6f573a 66%, var(--umber) 76%, var(--umber) 100%);
  }
  .logo-panel {
    position: absolute;
    left: 11px;
    top: 92px;
    width: 642px;
    height: 124px;
    background: var(--peach-light);
    box-shadow: 0 4px 10px rgba(60, 40, 10, 0.28);
    transform: rotate(-7deg);
    transform-origin: left top;
  }
  .company-name {
    position: absolute;
    left: 88px;
    top: 16px;
    font-family: "Barlow", sans-serif;
    font-weight: 600;
    color: var(--brand-orange);
    line-height: 1;
  }
  .company-name .name-main {
    display: block;
    font-size: 56px;
    letter-spacing: 1px;
  }
  .company-name .name-sub {
    display: block;
    font-size: 29px;
    letter-spacing: 3px;
    margin-top: 4px;
    margin-left: 52px;
  }
  .services-bar {
    position: absolute;
    left: 8px;
    top: 266px;
    width: 700px;
    height: 56px;
    background: var(--navy-ink);
    box-shadow: 0 5px 10px rgba(40, 25, 5, 0.35);
    transform: rotate(-11.5deg);
    transform-origin: left top;
    font-family: "Fira Sans Extra Condensed", sans-serif;
    font-weight: 700;
    font-size: 30px;
    color: var(--white);
    text-align: center;
    line-height: 56px;
    letter-spacing: 0.3px;
  }
  .tagline-bar {
    position: absolute;
    left: 150px;
    top: -31px;
    width: 262px;
    height: 31px;
    background: var(--burnt-orange);
    font-size: 24px;
    line-height: 31px;
    color: var(--tag-ink);
    letter-spacing: 0.5px;
    text-align: center;
  }
  .photo {
    position: absolute;
    overflow: hidden;
  }
  .photo-flood {
    left: 730px;
    top: -420px;
    width: 760px;
    height: 420px;
    border-bottom: 6px solid var(--frame-white);
    background: linear-gradient(200deg, #6b6d70 0%, #4c4d50 55%, #2d2e31 100%);
    transform: rotate(35deg);
    transform-origin: left bottom;
    box-shadow: 0 4px 12px rgba(0, 0, 0, 0.4);
  }
  .photo-debris {
    left: 858px;
    top: 205px;
    width: 150px;
    height: 210px;
    border: 10px solid var(--frame-orange);
    background: linear-gradient(170deg, #6d5a48 0%, #4a3d32 50%, #5b6b78 100%);
    transform: rotate(4deg);
    box-shadow: 0 4px 10px rgba(0, 0, 0, 0.45);
  }
  .photo-firefighter {
    left: 900px;
    top: 133px;
    width: 400px;
    height: 400px;
    border: 14px solid var(--alarm-red);
    background: radial-gradient(ellipse at 45% 40%, #4a4f4a 0%, #2b2d2b 45%, #1a1210 75%, #7a2a10 100%);
    transform: rotate(-28deg);
    transform-origin: left top;
    box-shadow: 0 4px 14px rgba(0, 0, 0, 0.5);
  }
</style>
</head>
<body>
  <main class="banner">
    <div class="photo photo-flood" role="img" aria-label="Photo of a car half submerged in floodwater"></div>
    <div class="photo photo-debris" role="img" aria-label="Photo of wooden storm debris"></div>
    <div class="photo photo-firefighter" role="img" aria-label="Photo of a firefighter in breathing gear amid sparks"></div>

    <div class="logo-panel">
      <h1 class="company-name">
        <span class="name-main">VELMAR BROOK</span>
        <span class="name-sub">CLAIM SERVICE, INC.</span>
      </h1>
    </div>

    <div class="services-bar">
      <div class="tagline-bar">WHEN IT HAPPENS</div>
      Accidents, Disasters, Fire, Flood, Wind, Property &amp; Liability
    </div>
  </main>
</body>
</html>
```